Design a BOLD Ad Design for Fitness Club

We are fitness facility that is about to run our new "Bright Parent Reboot" program and we need a bold design created for an ad that will run on Instagram and Facebook.

The ad needs to be eye catching, easy to read and attractive so that someone stops scrolling and clicks to join.

The add needs to be sized to 1080 x 1080, include our logo and the text "Bright Parent Reboot" and "Starting September 23rd"

I have included an example photo, which is to be used as an example only of a design style that stands out to us, (colors, female photo style, etc)

I have also included our logo, which the yellow color can be changed for this design.

Thank you and we look forward to seeing your design.

```html
<!DOCTYPE html>
<html lang="en">
<head>
<meta charset="UTF-8">
<title>PulseForge – Bright Parent Reboot</title>
<link href="https://fonts.googleapis.com/css2?family=Archivo:wght@700;800&family=Yellowtail&display=swap" rel="stylesheet">
<style>
  :root {
    --purple-deep: #5a006c;
    --purple: #6d0a7c;
    --purple-text: #680a78;
    --yellow: #f7c900;
    --white: #ffffff;
    --band: #e4e6ea;
    --dot: #ffffff;
  }
  * { margin: 0; padding: 0; box-sizing: border-box; }
  html, body { width: 1200px; height: 1200px; overflow: hidden; }
  body { background: var(--purple); font-family: "Archivo", Arial, sans-serif; }
  .ad {
    position: relative;
    width: 1200px; height: 1200px;
    overflow: hidden;
    background: linear-gradient(180deg, var(--purple-deep) 0%, var(--purple) 100%);
  }
  .brand {
    position: absolute; left: 72px; top: 74px;
    font-weight: 800; font-size: 76px; line-height: 1;
    color: var(--yellow); letter-spacing: -1px;
  }
  .dots { position: absolute; }
  .dots--top { left: 872px; top: 62px; }
  .dots--left { left: 200px; top: 340px; }

  .headline { position: absolute; left: 0; top: 0; width: 1200px; height: 520px; }
  .headline__word {
    position: absolute; font-weight: 800; color: var(--white);
    line-height: 1; letter-spacing: -1px;
  }
  .headline__word--first { right: 160px; top: 168px; font-size: 98px; }
  .headline__word--last { right: 106px; top: 382px; font-size: 98px; }
  .headline__script {
    position: absolute; right: 80px; top: 190px;
    font-family: "Yellowtail", cursive;
    font-size: 210px; line-height: 1; color: var(--yellow);
    transform: rotate(-4deg);
  }

  .start-label {
    position: absolute; left: 773px; top: 596px;
    font-weight: 800; font-size: 50px; color: var(--white); letter-spacing: -0.5px;
  }
  .start-date {
    position: absolute; left: 640px; top: 675px;
    width: 473px; height: 87px; border-radius: 44px;
    background: var(--yellow);
    display: flex; align-items: center; justify-content: center;
    font-weight: 800; font-size: 50px; color: var(--purple-text); letter-spacing: -0.5px;
  }

  .band { position: absolute; left: 0; top: 940px; }

  .cta {
    position: absolute; left: 595px; top: 1026px;
    display: flex; align-items: center; gap: 30px;
  }
  .cta__label {
    font-weight: 800; font-size: 60px; color: var(--purple-text); letter-spacing: 1px;
  }

  .ring { position: absolute; left: 40px; top: 430px; }
  .photo {
    position: absolute; left: 100px; top: 430px;
    width: 470px; height: 770px;
    border-radius: 200px 200px 0 0;
    background: linear-gradient(180deg, #3a2420 0%, #a86a48 22%, #b97a55 40%, #56646b 62%, #4a565c 100%);
  }
</style>
</head>
<body>
<main class="ad">
  <div class="brand">PulseForge</div>

  <svg class="dots dots--top" width="260" height="50" viewBox="0 0 260 50" aria-hidden="true">
    <g fill="var(--dot)">
      <circle cx="6" cy="6" r="3"/><circle cx="26" cy="6" r="3"/><circle cx="46" cy="6" r="3"/><circle cx="66" cy="6" r="3"/><circle cx="86" cy="6" r="3"/><circle cx="106" cy="6" r="3"/><circle cx="126" cy="6" r="3"/><circle cx="146" cy="6" r="3"/><circle cx="166" cy="6" r="3"/><circle cx="186" cy="6" r="3"/><circle cx="206" cy="6" r="3"/><circle cx="226" cy="6" r="3"/>
      <circle cx="28" cy="41" r="3"/><circle cx="48" cy="41" r="3"/><circle cx="68" cy="41" r="3"/><circle cx="88" cy="41" r="3"/><circle cx="108" cy="41" r="3"/><circle cx="128" cy="41" r="3"/><circle cx="148" cy="41" r="3"/><circle cx="168" cy="41" r="3"/><circle cx="188" cy="41" r="3"/><circle cx="208" cy="41" r="3"/><circle cx="228" cy="41" r="3"/><circle cx="248" cy="41" r="3"/>
    </g>
  </svg>
  <svg class="dots dots--left" width="260" height="50" viewBox="0 0 260 50" aria-hidden="true">
    <g fill="var(--dot)">
      <circle cx="6" cy="6" r="3"/><circle cx="26" cy="6" r="3"/><circle cx="46" cy="6" r="3"/><circle cx="66" cy="6" r="3"/><circle cx="86" cy="6" r="3"/><circle cx="106" cy="6" r="3"/><circle cx="126" cy="6" r="3"/><circle cx="146" cy="6" r="3"/><circle cx="166" cy="6" r="3"/><circle cx="186" cy="6" r="3"/><circle cx="206" cy="6" r="3"/>
      <circle cx="28" cy="41" r="3"/><circle cx="48" cy="41" r="3"/><circle cx="68" cy="41" r="3"/><circle cx="88" cy="41" r="3"/><circle cx="108" cy="41" r="3"/><circle cx="128" cy="41" r="3"/><circle cx="148" cy="41" r="3"/><circle cx="168" cy="41" r="3"/><circle cx="188" cy="41" r="3"/><circle cx="208" cy="41" r="3"/><circle cx="228" cy="41" r="3"/>
    </g>
  </svg>

  <h1 class="headline">
    <span class="headline__word headline__word--first">BRIGHT</span>
    <span class="headline__script">Parent</span>
    <span class="headline__word headline__word--last">REBOOT</span>
  </h1>

  <p class="start-label">Starting</p>
  <p class="start-date">September 23rd</p>

  <svg class="band" width="1200" height="210" viewBox="0 0 1200 210" aria-hidden="true">
    <path fill="var(--band)" d="M0 8 L300 4 L620 10 L900 2 L1200 6 L1200 196 L900 204 L600 198 L300 206 L0 200 Z"/>
  </svg>

  <div class="cta">
    <svg width="190" height="64" viewBox="0 0 190 64" aria-hidden="true">
      <g fill="var(--purple-text)">
        <path d="M0 0 H22 L44 32 L22 64 H0 L22 32 Z"/>
        <path d="M36 0 H58 L80 32 L58 64 H36 L58 32 Z"/>
        <path d="M72 0 H94 L116 32 L94 64 H72 L94 32 Z"/>
        <path d="M108 0 H130 L152 32 L130 64 H108 L130 32 Z"/>
        <path d="M144 0 H166 L188 32 L166 64 H144 L166 32 Z"/>
      </g>
    </svg>
    <span class="cta__label">JOIN NOW</span>
  </div>

  <svg class="ring" width="580" height="480" viewBox="0 0 580 480" aria-hidden="true">
    <circle cx="290" cy="230" r="262" fill="none" stroke="var(--yellow)" stroke-width="14"/>
  </svg>
  <div class="photo" role="img" aria-label="Smiling woman in a grey tank top holding two purple dumbbells"></div>
</main>
</body>
</html>
```